Need a Crisps (Potato Chips in US) and Popcorns Logo, Artwork and Packaging Design

I want to package my home made crisps and popcorns. The crisps will be going by the name ZapZoz (Ks are capital) and the popcorns by the name bumbim (Should all be in same case, either all small or all caps - I leave it to designer's choice).

Crisps:
I want both a logo that will be associated with the product and a package design with the logo embedded. The logo should be playful and striking.

The packaging for the crisps should be to the standards of international brands like Vorn, Flumbix, Garvelo, etc. Package type is the pouch based packages.

The colours should be vibrant. We are limited to 4 colours in the design due to printing costs. So the designer should use a mixture that is striking especially to children and young adults.

Incorporation of animal artwork is allowed as long as it does not infringe on IPs.

Popcorns:
This one is less intensive and only requires a logo and package design like the one used in movie halls.

Target Market(s)

Kids and young adults

Industry/Entity Type

Food Production

Logo Text

ZapZoz for crisps and bumbim for popcorn

Colors

Designer to choose colors to be used in the design.

Requirements
Must have
• Playful font and colours
Nice to have
• Distinguishing artwork

```html
<!DOCTYPE html>
<html lang="en">
<head>
<meta charset="utf-8">
<title>ZapZoz Potatoes Crisps Pouch</title>
<link rel="stylesheet" href="https://fonts.googleapis.com/css2?family=Open+Sans:ital,wght@0,800;1,400&display=swap">
<style>
  :root {
    --bg: #ffffff;
    --pouch: #000000;
    --sheen: #9a9a9a;
    --glow: #303030;
    --orange: #e8782a;
    --white: #ffffff;
    --crisp-light: #e9a35c;
    --crisp-deep: #c4602a;
  }
  html, body {
    margin: 0;
    width: 742px;
    height: 1200px;
    overflow: hidden;
    background: var(--bg);
  }
  .canvas {
    position: relative;
    width: 742px;
    height: 1200px;
    overflow: hidden;
  }
  .pouch-shape {
    position: absolute;
    inset: 0;
  }
  .brand-mark {
    position: absolute;
    left: 160px;
    top: 250px;
    display: flex;
    align-items: center;
    gap: 6px;
    font-family: "Open Sans", sans-serif;
    font-weight: 800;
    font-size: 20px;
    color: var(--orange);
  }
  .brand-mark .dot {
    width: 10px;
    height: 10px;
    border-radius: 50%;
    background: var(--orange);
  }
  .title-frame {
    position: absolute;
    left: 92px;
    top: 408px;
    width: 556px;
    height: 136px;
    box-sizing: border-box;
    border: 7px solid var(--orange);
    border-radius: 14px;
    background: var(--pouch);
    transform: rotate(-6deg);
    transform-origin: center;
    display: flex;
    align-items: center;
    justify-content: center;
  }
  .wordmark {
    font-family: "Open Sans", sans-serif;
    font-weight: 800;
    font-size: 104px;
    line-height: 1;
    letter-spacing: -1px;
    color: var(--white);
    margin-top: -8px;
  }
  .crisps-photo {
    position: absolute;
    left: 160px;
    top: 565px;
    width: 458px;
    height: 258px;
    border-radius: 48% 52% 40% 44% / 55% 50% 45% 50%;
    background: radial-gradient(ellipse at 45% 50%, var(--crisp-light) 0%, var(--crisp-deep) 70%, rgba(196,96,42,0) 100%);
  }
  .product-name {
    position: absolute;
    left: 0;
    width: 742px;
    top: 868px;
    text-align: center;
    font-family: "Open Sans", sans-serif;
    font-style: italic;
    font-weight: 400;
    font-size: 50px;
    color: var(--white);
    letter-spacing: 0.5px;
  }
</style>
</head>
<body>
<div class="canvas">
  <svg class="pouch-shape" width="742" height="1200" viewBox="0 0 742 1200" aria-hidden="true">
    <defs>
      <radialGradient id="spotlight" cx="0.5" cy="0.5" r="0.5">
        <stop offset="0" stop-color="#303030"/>
        <stop offset="1" stop-color="#000000" stop-opacity="0"/>
      </radialGradient>
      <clipPath id="pouch-clip">
        <path d="M4 136 Q2 128 14 128 L734 134 Q738 134 736 142
         Q716 300 668 470 Q640 560 668 640 Q700 760 688 900
         Q690 1020 712 1120 Q720 1160 700 1180 Q560 1170 380 1176
         Q200 1180 44 1180 Q30 1170 50 1160 Q80 1140 84 1090
         Q96 980 110 930 Q80 820 84 700 Q80 580 44 440 Q10 300 4 136 Z"/>
      </clipPath>
    </defs>
    <path class="seal-strip" fill="var(--pouch)"
      d="M24 120 L24 22 L36 44 L48 22 L60 44 L72 22 L84 44 L96 22 L108 44 L120 22 L132 44 L144 22 L156 44 L168 22 L180 44 L192 22 L204 44 L216 22 L228 44 L240 22 L252 44 L264 22 L276 44 L288 22 L300 44 L312 22 L324 44 L336 22 L348 44 L360 22 L372 44 L384 22 L396 44 L408 22 L420 44 L432 22 L444 44 L456 22 L468 44 L480 22 L492 44 L504 22 L516 44 L528 22 L540 44 L552 22 L564 44 L576 22 L588 44 L600 22 L612 44 L624 22 L636 44 L648 22 L660 44 L672 22 L684 44 L690 28 L716 120 Z"/>
    <path class="pouch-body" fill="var(--pouch)"
      d="M4 136 Q2 128 14 128 L734 134 Q738 134 736 142
         Q716 300 668 470 Q640 560 668 640 Q700 760 688 900
         Q690 1020 712 1120 Q720 1160 700 1180 Q560 1170 380 1176
         Q200 1180 44 1180 Q30 1170 50 1160 Q80 1140 84 1090
         Q96 980 110 930 Q80 820 84 700 Q80 580 44 440 Q10 300 4 136 Z"/>
    <g clip-path="url(#pouch-clip)">
      <ellipse cx="390" cy="580" rx="260" ry="240" fill="url(#spotlight)"/>
      <g class="pouch-sheen" fill="none" stroke="var(--sheen)" stroke-linecap="round" opacity="0.55">
        <path d="M196 300 Q214 520 206 720 Q200 900 216 1070" stroke-width="5"/>
        <path d="M660 140 Q640 300 636 480" stroke-width="6"/>
        <path d="M630 690 Q600 900 610 1060" stroke-width="4"/>
        <path d="M500 1030 Q520 1100 540 1160" stroke-width="3"/>
      </g>
    </g>
  </svg>

  <div class="brand-mark"><span class="dot"></span>ZapZoz</div>

  <div class="title-frame"><span class="wordmark">ZapZoz</span></div>

  <div class="crisps-photo" role="img" aria-label="Photograph of a pile of golden seasoned potato crisps"></div>

  <div class="product-name">Potatoes Crisps</div>
</div>
</body>
</html>
```